Pro-life non-profit needs a dynamic poster design for their Christmas Gala.

We need a poster design which plays off the name of the event, The Winter Lantern. The Winter Lantern, of course is the Baby Jesus. Our cause supports unborn children in Iowa. The gala will include a concert of popular Christmas music sung by top soloists backed by an orchestra. An original commissioned song, The Winter Lantern, will be premiered. Purple and gold colors immediately come to mind, but a designer should not feel constrained on colors. We need an editable design w/fonts. Photoshop w/layers or Illustrator files are good.

```html
<!DOCTYPE html>
<html lang="en">
<head>
<meta charset="utf-8">
<title>The Winter Lantern — A Pro-Life Christmas Gala</title>
<link href="https://fonts.googleapis.com/css2?family=Cinzel:wght@500;700&family=Playfair+Display:wght@400;600&family=Montserrat:wght@500;600;700&display=swap" rel="stylesheet">
<style>
  :root {
    --cream: #fbf8f2;
    --cream-glow: #efe9de;
    --crimson: #8e1020;
    --crimson-deep: #5c0812;
    --crimson-light: #b3202f;
    --gold: #d9a94a;
    --gold-light: #f3d58a;
    --gold-dark: #a9792a;
    --white: #ffffff;
    --ink: #3a2a1a;
  }
  * { box-sizing: border-box; margin: 0; padding: 0; }
  html, body { width: 900px; height: 1200px; overflow: hidden; background: var(--crimson-deep); }
  .poster {
    position: relative; width: 900px; height: 1200px; overflow: hidden;
    background: radial-gradient(ellipse at 50% 45%, var(--crimson-light) 0%, var(--crimson) 45%, var(--crimson-deep) 100%);
    font-family: 'Montserrat', sans-serif; color: var(--white);
  }
  .header-shape { position: absolute; inset: 0; width: 900px; height: 1200px; }
  .bokeh-glow {
    position: absolute; left: 40px; top: 30px; width: 820px; height: 250px;
    background: radial-gradient(ellipse at 30% 40%, var(--white) 0%, transparent 60%),
                radial-gradient(ellipse at 75% 30%, var(--white) 0%, transparent 55%);
    opacity: .7;
  }
  .header { position: absolute; top: 0; left: 0; width: 900px; text-align: center; }
  .org-name {
    display: inline-flex; align-items: center; gap: 12px; margin-top: 58px;
    font-family: 'Playfair Display', serif; font-weight: 600; font-size: 46px; color: var(--ink);
  }
  .org-mark { width: 16px; height: 16px; border-radius: 50%; background: var(--gold-dark); }
  .presents {
    margin-top: 10px; font-family: 'Playfair Display', serif; font-size: 32px; color: var(--gold-dark);
  }
  .banquet {
    margin-top: 4px; font-family: 'Playfair Display', serif; font-size: 34px; color: var(--gold-dark);
  }
  .ornaments {
    position: absolute; left: 90px; top: 330px; width: 720px; height: 90px;
    background: radial-gradient(circle at 12% 50%, rgba(243,213,138,.35) 0 22px, transparent 24px),
                radial-gradient(circle at 88% 50%, rgba(243,213,138,.35) 0 22px, transparent 24px),
                radial-gradient(circle at 30% 60%, rgba(243,213,138,.25) 0 14px, transparent 16px),
                radial-gradient(circle at 70% 60%, rgba(243,213,138,.25) 0 14px, transparent 16px);
  }
  .title {
    position: absolute; top: 400px; left: 0; width: 900px; text-align: center;
    font-family: 'Cinzel', serif; font-weight: 700; color: var(--gold-light);
    text-shadow: 0 0 18px rgba(243,213,138,.45), 0 3px 0 var(--gold-dark);
    line-height: 1;
  }
  .title-the { font-size: 96px; display: block; }
  .title-main { font-size: 74px; display: block; margin-top: 14px; letter-spacing: 1px; }
  .gala-line {
    position: absolute; top: 610px; width: 900px; text-align: center;
    font-weight: 600; font-size: 33px; letter-spacing: 1px;
  }
  .details {
    position: absolute; top: 780px; left: 130px; width: 640px;
    display: flex; justify-content: space-between; font-size: 15px; font-weight: 600; line-height: 1.5;
  }
  .details-left { text-align: left; }
  .details-right { text-align: right; }
  .speaker { position: absolute; top: 890px; width: 900px; text-align: center; font-size: 24px; font-weight: 700; }
  .speaker-label { color: var(--gold-light); }
  .seating {
    position: absolute; top: 960px; width: 900px; text-align: center;
    font-size: 30px; font-weight: 700; color: var(--gold-light); letter-spacing: 1px;
  }
  .order { position: absolute; top: 1022px; width: 900px; text-align: center; font-size: 16px; font-weight: 600; }
  .order-label { color: var(--gold-light); }
  .contacts {
    position: absolute; top: 1050px; width: 900px; display: flex; justify-content: center; gap: 26px;
    font-size: 14px; font-weight: 500;
  }
  .contact { display: inline-flex; align-items: center; gap: 7px; }
  .contact svg { width: 16px; height: 16px; fill: var(--gold-light); }
</style>
</head>
<body>
<main class="poster">
  <svg class="header-shape" viewBox="0 0 900 1200" aria-hidden="true">
    <path d="M0 0 H900 V300 Q780 300 720 315 Q600 345 450 370 Q300 345 180 315 Q120 300 0 300 Z" fill="var(--cream)"/>
    <path d="M0 300 Q120 300 180 315 Q300 345 450 370 Q600 345 720 315 Q780 300 900 300" fill="none" stroke="var(--gold)" stroke-width="5"/>
    <rect x="26" y="26" width="848" height="1148" fill="none" stroke="var(--gold)" stroke-width="3"/>
    <rect x="38" y="38" width="824" height="1124" fill="none" stroke="var(--gold-dark)" stroke-width="1.5"/>
    <line x1="250" y1="730" x2="650" y2="730" stroke="var(--gold)" stroke-width="2"/>
    <circle cx="450" cy="730" r="5" fill="var(--gold)"/>
  </svg>
  <div class="bokeh-glow" aria-hidden="true"></div>
  <header class="header">
    <div class="org-name"><span class="org-mark"></span>Heartland Life Alliance</div>
    <p class="presents">Presents</p>
    <p class="banquet">The Tenth Annual Fundraising Banquet</p>
  </header>
  <div class="ornaments" role="img" aria-label="Hanging gold Christmas baubles and snowflakes"></div>
  <h1 class="title">
    <span class="title-the">The</span>
    <span class="title-main">Winter Lantern</span>
  </h1>
  <p class="gala-line">A PRO-LIFE CHRISTMAS GALA</p>
  <section class="details">
    <div class="details-left">
      SATURDAY, NOVEMBER 21ST, 2020<br>
      DOORS OPEN AT 5:30PM<br>
      MAPLE GROVE HALL, WEST FAIRVIEW, IA
    </div>
    <div class="details-right">
      $60 PERSON • $500 TABLE OF TEN<br>
      COCKTAILS • DINNER • CHRISTMAS CONCERT
    </div>
  </section>
  <p class="speaker"><span class="speaker-label">SPECIAL GUEST SPEAKER:</span> BISHOP THOMAS ALBRIGHT</p>
  <p class="seating">SEATING LIMITED • RESERVATIONS NEEDED</p>
  <p class="order"><span class="order-label">ORDER TICKETS ONLINE:</span> www.HeartlandLifeAlliance.org</p>
  <div class="contacts">
    <span class="contact">
      <svg viewBox="0 0 24 24" aria-hidden="true"><path d="M6.6 10.8a15 15 0 0 0 6.6 6.6l2.2-2.2a1 1 0 0 1 1-.25 11.4 11.4 0 0 0 3.6.57 1 1 0 0 1 1 1V20a1 1 0 0 1-1 1A17 17 0 0 1 3 4a1 1 0 0 1 1-1h3.5a1 1 0 0 1 1 1c0 1.25.2 2.45.57 3.6a1 1 0 0 1-.25 1z"/></svg>
      515-555-0142
    </span>
    <span class="contact">
      <svg viewBox="0 0 24 24" aria-hidden="true"><path d="M3 5h18a1 1 0 0 1 1 1v12a1 1 0 0 1-1 1H3a1 1 0 0 1-1-1V6a1 1 0 0 1 1-1zm9 7.5L4 7.6V8l8 5 8-5v-.4z"/></svg>
      events@heartlandlife.org
    </span>
  </div>
</main>
</body>
</html>
```